New Label Design Project for Tinkers hollow wines

I would like to purchase a customized version of a design you have previously submitted - https://www.artpitchhub.com.au/design/57302946

We need a label that that we can use for our new vintage shiraz, Merlot and Pinot Noir products. This Label will be just 1 label that will be front and back label.
Please see attached

Target Market(s)

young and old wine drinkers

Industry/Entity Type

Wine

Colors

Designer to choose colors to be used in the design.

Requirements
Must have
• logo but also is a bit funky
Nice to have
• mixture of Funky and Modern

```html
<!DOCTYPE html>
<html lang="en">
<head>
<meta charset="utf-8">
<title>Tinkers Hollow Wines – Shiraz Label</title>
<link rel="stylesheet" href="https://fonts.googleapis.com/css2?family=Montserrat:wght@200;700&family=Permanent+Marker&display=swap">
<style>
  :root {
    --paper: #ffffff;
    --wine: #260e15;
    --gold: #cfb97a;
    --gold-text: #c9b26e;
    --ink: #1c0b10;
    --trim: #e31e24;
  }
  * { margin: 0; padding: 0; box-sizing: border-box; }
  html, body {
    width: 1200px; height: 1200px; overflow: hidden;
    background: var(--paper);
  }
  .label {
    position: absolute; left: 250px; top: 146px;
    width: 700px; height: 908px;
    background: var(--paper);
  }
  .label__trim {
    position: absolute; inset: 0;
    border: 1.5px solid var(--trim);
    pointer-events: none; z-index: 5;
  }
  .label__splash {
    position: absolute; inset: 0; width: 700px; height: 908px;
  }
  .brand {
    position: absolute; left: 0; right: 0; top: 95px;
    text-align: center; color: var(--gold-text);
    font-family: "Permanent Marker", cursive;
  }
  .brand__dot {
    display: block; margin: 0 auto 20px;
    width: 56px; height: 56px; border-radius: 50%;
    background: var(--gold-text);
  }
  .brand__name {
    font-size: 64px; line-height: 62px; letter-spacing: 0.14em;
    text-transform: uppercase;
  }
  .variety {
    position: absolute; left: 0; right: 0; top: 492px;
    text-align: center; color: var(--paper);
    font-family: "Permanent Marker", cursive;
    font-size: 50px; letter-spacing: 0.32em; padding-left: 0.32em;
    z-index: 2;
  }
  .vintage {
    position: absolute; left: 0; right: 0; top: 548px;
    text-align: center; color: var(--paper);
    font-family: "Montserrat", sans-serif; font-weight: 200;
    font-size: 48px; letter-spacing: 0.1em; z-index: 2;
  }
  .region {
    position: absolute; left: 0; right: 0; top: 700px;
    text-align: center; color: var(--paper);
    font-family: "Montserrat", sans-serif; font-weight: 200;
    font-size: 46px; letter-spacing: 0.36em; padding-left: 0.36em;
    text-transform: uppercase; z-index: 2;
  }
  .origin-band {
    position: absolute; left: 0; right: 0; top: 795px; height: 51px;
    background: var(--gold);
    display: flex; align-items: center; justify-content: center;
    font-family: "Montserrat", sans-serif; font-weight: 700;
    font-size: 27px; letter-spacing: 0.09em; color: var(--ink);
    text-transform: uppercase; z-index: 2;
  }
</style>
</head>
<body>
  <main class="label">
    <svg class="label__splash" viewBox="0 0 700 908" role="img" aria-label="Dark wine-coloured brush splash artwork">
      <polygon fill="var(--wine)" points="0,520 120,440 230,370 330,318 370,300 420,330 520,310 600,350 650,345 700,380 700,520 660,600 690,640 640,720 700,760 640,800 560,860 480,908 0,908"/>
    </svg>

    <header class="brand">
      <span class="brand__dot"></span>
      <h1 class="brand__name">Tinkers<br>Hollow</h1>
    </header>

    <p class="variety">Shiraz</p>
    <p class="vintage">2007</p>
    <p class="region">Mt. Corrigan</p>
    <p class="origin-band">Wine of Australia</p>

    <div class="label__trim"></div>
  </main>
</body>
</html>
```